Bakery Business Cards

We are in need of business cards for our bakery business--something non-generic that reflects our business and will stand out. We are a wholesale bakery that primarily services in-store bakeries, casinos, schools, distributors, and fund-raising companies. The family business was founded in 1960. (www.dorvalbakehouse.example)

```html
<!DOCTYPE html>
<html lang="en">
<head>
<meta charset="utf-8">
<title>Dorval Bakehouse – Business Cards</title>
<link rel="stylesheet" href="https://fonts.googleapis.com/css2?family=Libre+Baskerville:ital,wght@0,400;0,700;1,400&display=swap">
<style>
  :root {
    --backdrop: #a9a9a9;
    --card-white: #ffffff;
    --brand-blue: #0047b8;
    --ink-blue: #1a4fb8;
    --plate: #f4efea;
    --wood-light: #e6d2b6;
    --wood: #d4b48a;
    --crust: #c9975a;
    --text-light: #ffffff;
  }
  html, body {
    margin: 0;
    padding: 0;
    width: 1200px;
    height: 1000px;
    overflow: hidden;
    background: var(--backdrop);
    font-family: "Libre Baskerville", Georgia, serif;
  }
  .canvas {
    position: relative;
    width: 1200px;
    height: 1000px;
  }
  .card {
    position: absolute;
    left: 294px;
    width: 613px;
    height: 351px;
    border-radius: 22px;
    overflow: hidden;
    box-shadow: 0 24px 40px rgba(0, 0, 0, 0.28);
  }
  .card--front { top: 93px; background: var(--card-white); }
  .card--back { top: 547px; background: var(--brand-blue); }

  .photo {
    position: absolute;
    top: 0;
    height: 100%;
  }
  .card--front .photo {
    right: 0;
    width: 330px;
    background: linear-gradient(90deg, var(--card-white) 0%, var(--plate) 22%, var(--wood-light) 50%, var(--plate) 68%, var(--wood) 88%, var(--crust) 100%);
  }
  .card--back .photo {
    left: 0;
    width: 320px;
    background: linear-gradient(90deg, var(--crust) 0%, var(--plate) 22%, var(--wood-light) 45%, var(--plate) 60%, var(--brand-blue) 100%);
  }

  .brand-name {
    position: absolute;
    margin: 0;
    font-weight: 700;
    font-size: 48px;
    line-height: 1.12;
    text-align: center;
  }
  .card--front .brand-name {
    left: 36px;
    top: 112px;
    width: 320px;
    color: var(--ink-blue);
  }
  .card--back .brand-name {
    left: 258px;
    top: 130px;
    width: 310px;
    color: var(--text-light);
  }

  .tagline {
    position: absolute;
    left: 36px;
    top: 280px;
    width: 320px;
    margin: 0;
    text-align: center;
    font-style: italic;
    font-size: 19px;
    color: var(--ink-blue);
  }

  .badge {
    position: absolute;
    left: 522px;
    top: 100px;
    width: 74px;
    height: 74px;
  }

  .contact {
    position: absolute;
    left: 182px;
    top: 300px;
    width: 420px;
    margin: 0;
    text-align: center;
    font-size: 9.8px;
    line-height: 15px;
    white-space: nowrap;
    color: var(--text-light);
  }
</style>
</head>
<body>
<main class="canvas">
  <section class="card card--front" aria-label="Business card front">
    <div class="photo" role="img" aria-label="Overhead photo of a slice of cherry pie on a white plate with a fork, on a wooden table"></div>
    <h1 class="brand-name">Dorval<br>Bakehouse</h1>
    <p class="tagline">Serving Sweetness Since 1960</p>
  </section>

  <section class="card card--back" aria-label="Business card back">
    <div class="photo" role="img" aria-label="Overhead photo of a slice of cherry pie on a white plate with a fork, on a wooden table"></div>
    <h2 class="brand-name">Dorval<br>Bakehouse</h2>
    <svg class="badge" viewBox="0 0 74 74" aria-hidden="true">
      <circle cx="37" cy="37" r="35" fill="none" stroke="#ffffff" stroke-width="2"/>
    </svg>
    <p class="contact">(405) 555-0142 · sales@dorvalbakehouse.example · www.dorvalbakehouse.example<br>1870 Harlow Ave, Fairmont, OK 73199</p>
  </section>
</main>
</body>
</html>
```